BELO Investment Services Business Cards
Business Cards 2011
Professional
Marcus Tillery
President
1877 Wendover Lane., Suite 300
Lakemont, CA 90217
877-560-BELO (2356)
marcus.tillery@qmx-mail.com
www.belohq.com
CA Insurance # 0K48213
Ensure all text is editable. Please also put this disclosure at the bottom in smaller font size to read:
"Marcus Tillery is a registered representative with and offering securities through QMX Financial.
Member NORVA/TEBU
BELO Investment Services Logo
Logo AI file
logo AI file 2.0

```html
<!DOCTYPE html>
<html lang="en">
<head>
<meta charset="utf-8">
<title>BELO Investment Services – Business Card</title>
<link href="https://fonts.googleapis.com/css2?family=Cinzel:wght@400;600&family=Arimo&display=swap" rel="stylesheet">
<style>
  :root {
    --page: #ffffff;
    --ink: #111111;
    --night: #0c0c0c;
    --olive: #8b9b25;
    --olive-deep: #6f7d17;
    --pearl: #e9ece0;
    --steel: #b9c3cc;
  }
  html, body {
    margin: 0;
    width: 1200px;
    height: 835px;
    overflow: hidden;
    background: var(--page);
  }
  .card {
    position: absolute;
    left: 564px;
    top: 214px;
    width: 624px;
    height: 362px;
    background: linear-gradient(160deg, var(--olive) 0%, var(--olive-deep) 100%);
    overflow: hidden;
    font-family: "Cinzel", serif;
    color: var(--ink);
  }
  .card__swoosh {
    position: absolute;
    inset: 0;
  }
  .brand {
    position: absolute;
    left: 34px;
    top: 28px;
    width: 240px;
    text-align: center;
  }
  .brand__name {
    font-size: 50px;
    font-weight: 600;
    letter-spacing: 6px;
    line-height: 1;
    color: var(--steel);
  }
  .brand__tagline {
    margin-top: 12px;
    font-size: 17px;
    letter-spacing: 0.5px;
    color: var(--pearl);
  }
  .contact {
    position: absolute;
    right: 8px;
    top: 36px;
    width: 400px;
    text-align: right;
  }
  .contact__name {
    font-size: 20px;
    font-weight: 600;
    letter-spacing: 2px;
    line-height: 1.1;
  }
  .contact__role {
    font-size: 15px;
    letter-spacing: 3px;
    line-height: 1.3;
    margin-bottom: 30px;
  }
  .contact__line {
    font-size: 13px;
    letter-spacing: 1.4px;
    line-height: 23px;
    white-space: nowrap;
    color: var(--night);
  }
  .contact__line--gap { margin-top: 14px; }
  .disclosure {
    position: absolute;
    left: 12px;
    right: 12px;
    top: 322px;
    margin: 0;
    font-family: "Arimo", sans-serif;
    font-size: 10.5px;
    line-height: 1.25;
    text-align: center;
    color: var(--ink);
  }
</style>
</head>
<body>
  <section class="card" aria-label="BELO Investment Services business card">
    <svg class="card__swoosh" width="624" height="362" viewBox="0 0 624 362" aria-hidden="true">
      <path d="M0 0 H395 C 340 90, 270 250, 0 292 Z" fill="var(--night)"/>
      <path d="M395 0 C 340 90, 270 250, 0 292" fill="none" stroke="var(--pearl)" stroke-width="3"/>
    </svg>

    <div class="brand">
      <div class="brand__name">BELO</div>
      <div class="brand__tagline">Investment Services</div>
    </div>

    <div class="contact">
      <div class="contact__name">Marcus Tillery</div>
      <div class="contact__role">President</div>
      <div class="contact__line">1877 Wendover Lane., Suite 410</div>
      <div class="contact__line">Lakemont, CA 90217</div>
      <div class="contact__line contact__line--gap">Toll Free: 877-555-BELO (2356)</div>
      <div class="contact__line">Phone: 858-555-0148</div>
      <div class="contact__line">Fax: 858-555-0192</div>
      <div class="contact__line">marcus.tillery@qmx-mail.com</div>
      <div class="contact__line">www.belohq.com</div>
      <div class="contact__line">CA Insurance # 0K48213</div>
    </div>

    <p class="disclosure">"Marcus Tillery is a registered representative with and offering securities through QMX Financial. Member NORVA/TEBU</p>
  </section>
</body>
</html>
```